Landing page for web3 game airdrop

We need a specialist to create landing pages.

- Someone who understands the cycle of ideation > creation > measurement > adjustment > ideation > etc.
- Not one size fits all, but many segments/journeys.
- Experience with crypto and airdrops is a must.
- Experience with gaming and web3 is nice to have.

The landing page we need now is a page that explains our airdrop campaign and have people sign up.

Elements we want:
- Attention > Hero
- Interest > use case
- Desire > benefits
- Conviction > social proof/current success
- Action > CTA

Our website: https://velmora.com/
Current temporary landing page: https://7kqtz391.pagewisp.com/
Registration page: https://accounts.velmora.com/

For colors and fonts: keep to the colors of our website (velmora.com)
For background info: read our whitepaper.velmora.com

Target Market(s)

Web3 gamers, airdrop hunters, crypto interested

Font styles to use
Other font styles liked:
• keep the current ones on velmora.com

Colors

Designer to choose colors to be used in the design.

Requirements
Must have
• The flow as described: attention > interest > desire > conviction > action. If you have more ideas: of course welcome!
Nice to have
• Link with gaming, showing that we are special

```html
<!DOCTYPE html>
<html lang="en">
<head>
<meta charset="utf-8">
<title>Velmora – Airdrop Campaign</title>
<link href="https://fonts.googleapis.com/css2?family=Roboto+Condensed:wght@400;700&family=Roboto:wght@400;500&display=swap" rel="stylesheet">
<style>
:root{
  --bg:#1b1e33;
  --bg-deep:#151828;
  --band:#2f3060;
  --footer:#12131d;
  --purple:#6b53d6;
  --purple-glow:rgba(108,72,200,.55);
  --btn-fill:#2c2870;
  --gold:#c9a227;
  --text:#ffffff;
  --muted:#d5d6e4;
  --line:#3a3b52;
}
*{box-sizing:border-box;margin:0;padding:0}
html,body{width:1200px;height:3319px;overflow:hidden;background:var(--bg)}
body{font-family:"Roboto",sans-serif;color:var(--text)}
.page{position:relative;width:1200px;height:3319px;overflow:hidden;
  background:
    radial-gradient(ellipse 160px 260px at 1200px 870px,var(--purple-glow),transparent 70%),
    radial-gradient(ellipse 170px 260px at 0 1080px,var(--purple-glow),transparent 70%),
    radial-gradient(ellipse 140px 220px at 1200px 2150px,var(--purple-glow),transparent 70%),
    var(--bg)}
.abs{position:absolute}
.center{left:0;width:1200px;text-align:center}
.cond{font-family:"Roboto Condensed",sans-serif}

/* header */
.brand{left:111px;top:24px;font-family:"Roboto Condensed",sans-serif;font-weight:700;font-size:38px;letter-spacing:6px;color:var(--text)}
.menu{left:1060px;top:33px;width:28px;height:22px}
.menu span{display:block;height:2px;background:var(--gold);margin-bottom:7px}

/* hero */
.hero-art{left:0;top:0;width:1200px;height:720px;
  background:
    radial-gradient(ellipse 520px 140px at 600px 380px,rgba(40,140,170,.55),transparent 75%),
    radial-gradient(ellipse 700px 200px at 600px 440px,rgba(30,90,130,.45),transparent 75%),
    linear-gradient(180deg,#1e2238 0%,#2b3a55 35%,#244a66 52%,#202a48 75%,var(--bg) 100%)}
.hero-title{top:262px;font-family:"Roboto Condensed",sans-serif;font-weight:700;font-size:74px;line-height:1}
.hero-sub{top:376px;font-size:20px;line-height:33px;color:var(--muted)}
.btn{display:flex;align-items:center;justify-content:center;font-family:"Roboto Condensed",sans-serif;font-weight:700;font-size:13px;letter-spacing:.4px;color:var(--text);
  background:var(--btn-fill);border:2px solid var(--purple);border-radius:26px;box-shadow:0 0 16px var(--purple-glow)}
.hero-btn{left:535px;top:474px;width:131px;height:48px}

/* sections */
.section-title{font-family:"Roboto Condensed",sans-serif;font-weight:700;font-size:34px;letter-spacing:.5px}
.how-title{top:768px}
.how-sub{top:832px;font-size:18px;line-height:30px;color:var(--muted)}
.step{width:260px;text-align:center}
.step svg{display:block;margin:0 auto}
.step h3{font-family:"Roboto Condensed",sans-serif;font-weight:700;font-size:21px;margin-top:25px}
.step p{font-family:"Roboto Condensed",sans-serif;font-size:15.5px;line-height:23px;color:var(--muted);margin-top:14px}

.walk-title{top:1308px}
.video{left:187px;top:1400px;width:827px;height:434px;border:2px solid var(--purple);border-radius:22px;box-shadow:0 0 22px var(--purple-glow);overflow:hidden;
  background:radial-gradient(ellipse 400px 160px at 420px 380px,#2a4160,transparent 75%),linear-gradient(180deg,#1a1b3a,#141530)}
.video .shot-panel{position:absolute;left:62px;top:66px;width:292px;height:288px;border-radius:6px;background:linear-gradient(180deg,#2a2859,#231f4d)}
.video .shot-scene{position:absolute;left:362px;top:66px;width:396px;height:288px;border-radius:6px;background:radial-gradient(ellipse 200px 120px at 230px 150px,#3d6a3f,transparent 75%),linear-gradient(180deg,#1d2b2a,#10150f)}
.video .play{position:absolute;left:382px;top:180px}

.ben-title{top:1932px}
.benefit{width:200px;text-align:center}
.benefit svg{display:block;margin:0 auto;height:82px}
.benefit p{font-family:"Roboto Condensed",sans-serif;font-weight:700;font-size:18px;margin-top:26px}

/* cta band */
.band{left:0;top:2257px;width:1200px;height:385px;background:var(--band)}
.band-title{left:168px;top:2352px;font-family:"Roboto Condensed",sans-serif;font-weight:700;font-size:35px;line-height:48px}
.band-btn{left:169px;top:2488px;width:131px;height:49px}
.band-art{left:646px;top:2235px;width:428px;height:428px;border-radius:50%;border:3px solid var(--gold);
  background:radial-gradient(ellipse 180px 100px at 200px 300px,#3b3e48,transparent 75%),linear-gradient(180deg,#2a2f63 0%,#2d6a2e 25%,#1e3a23 50%,#252a30 80%,#1a1c24 100%)}

/* partners */
.partner{display:flex;align-items:center;gap:12px;font-family:"Roboto Condensed",sans-serif;font-weight:700;font-size:26px;color:#cfd0d8;letter-spacing:1px}
.partner i{display:block;width:30px;height:30px;border:3px solid #cfd0d8}

/* footer */
.footer{left:0;top:2958px;width:1200px;height:361px;background:var(--footer)}
.f-links{text-align:center;font-size:14px;line-height:26px;color:var(--muted)}
.divider{width:1px;height:232px;background:var(--line);top:3048px}
.news-title{top:3054px;font-family:"Roboto Condensed",sans-serif;font-weight:700;font-size:19px}
.email{left:438px;top:3110px;width:325px;height:44px;border-radius:3px;background:#23242f;display:flex;align-items:center;justify-content:space-between;padding:0 16px;font-size:15px;color:var(--muted)}
.socials{left:495px;top:3192px;display:flex;gap:5px}
.socials span{width:38px;height:38px;border:2px solid #e6e6ee;border-radius:50%}
.copy{top:3262px;font-size:14px;color:var(--muted)}
</style>
</head>
<body>
<div class="page">

  <div class="abs hero-art" role="img" aria-label="Game scene: a boat floating on a glowing sea at night under a cracked dark sky"></div>

  <header>
    <div class="abs brand">VELMORA</div>
    <div class="abs menu" aria-label="Menu"><span></span><span></span><span></span></div>
  </header>

  <section class="hero">
    <h1 class="abs center hero-title">Web3 Game Velmora</h1>
    <p class="abs center hero-sub">Duis aute irure dolor in reprehenderit in voluptate velit esse cillum dolore eu<br>fugiat nulla pariatur.</p>
    <a class="abs btn hero-btn">JOIN NOW</a>
  </section>

  <section class="how">
    <h2 class="abs center section-title how-title">HOW IT WORKS</h2>
    <p class="abs center how-sub">Velmora's airdrop campaign is massive!&nbsp; We drop 25 million $VLM worth $87,500<br>And you can easily join!</p>

    <div class="abs step" style="left:137px;top:924px">
      <svg width="146" height="164" viewBox="0 0 146 164"><polygon points="73,2 143,42 143,122 73,162 3,122 3,42" fill="none" stroke="#6b53d6" stroke-width="2"/>
        <g fill="none" stroke="#c9a227" stroke-width="4" stroke-linecap="round"><circle cx="71" cy="84" r="27"/><circle cx="71" cy="76" r="9"/><path d="M54 102c5-10 29-10 34 0"/><path d="M92 56v14M85 63h14"/></g></svg>
      <h3>Step 1</h3>
      <p>Sign up and confirm your email<br>address. Then secure your account<br>with a password.</p>
    </div>
    <div class="abs step" style="left:471px;top:924px">
      <svg width="146" height="164" viewBox="0 0 146 164"><polygon points="73,2 143,42 143,122 73,162 3,122 3,42" fill="none" stroke="#6b53d6" stroke-width="2"/>
        <g fill="none" stroke="#c9a227" stroke-width="3" stroke-linejoin="round"><path d="M72 52h34v28H88l-8 7v-7h-8z"/><path d="M42 72h30v24H56l-7 6v-6h-7z"/><path d="M60 96h22v18H70l-6 5v-5h-4z"/></g></svg>
      <h3>Step 2</h3>
      <p>Connect your socials (Chirp, Wirecast<br>or Guildhall) and your wallet.</p>
    </div>
    <div class="abs step" style="left:803px;top:924px">
      <svg width="146" height="164" viewBox="0 0 146 164"><polygon points="73,2 143,42 143,122 73,162 3,122 3,42" fill="none" stroke="#6b53d6" stroke-width="2"/>
        <g fill="none" stroke="#c9a227" stroke-width="4" stroke-linecap="round"><circle cx="62" cy="80" r="9"/><path d="M46 106c2-10 10-15 16-15s14 5 16 15z"/><circle cx="82" cy="70" r="10"/><path d="M78 86c8 0 14 4 16 10"/><path d="M94 100v16M86 108h16"/></g></svg>
      <h3>Step 3</h3>
      <p>Start doing missions and invite<br>your friends. The more Power you<br>earn, the larger your share of the<br>25 million $VLM.</p>
    </div>
  </section>

  <section class="walk">
    <h2 class="abs center section-title walk-title">WATCH THE WALKTHROUGH</h2>
    <div class="abs video">
      <div class="shot-panel" role="img" aria-label="Screen of the airdrop eligibility checklist"></div>
      <div class="shot-scene" role="img" aria-label="Game scene of a jungle with a waterfall"></div>
      <svg class="play" width="64" height="64" viewBox="0 0 64 64"><circle cx="32" cy="32" r="29" fill="none" stroke="#fff" stroke-width="3"/><path d="M26 20l18 12-18 12z" fill="none" stroke="#fff" stroke-width="3" stroke-linejoin="round"/></svg>
    </div>
  </section>

  <section class="benefits">
    <h2 class="abs center section-title ben-title">OUR BENEFITS</h2>
    <div class="abs benefit" style="left:185px;top:2028px">
      <svg viewBox="0 0 90 82" width="90"><g fill="none" stroke="#c9a227" stroke-width="3"><rect x="8" y="2" width="34" height="76"/><path d="M16 2v76M2 78h46"/><rect x="44" y="52" width="40" height="24" rx="10"/><path d="M54 64h8M58 60v8"/><circle cx="74" cy="62" r="2"/><circle cx="74" cy="68" r="2"/></g></svg>
      <p>Lorem ipsum dolor sit</p>
    </div>
    <div class="abs benefit" style="left:395px;top:2028px">
      <svg viewBox="0 0 104 82" width="104"><g fill="none" stroke="#c9a227" stroke-width="3"><rect x="2" y="24" width="100" height="36" rx="18"/><path d="M14 34l12 8-12 8z"/></g><text x="62" y="50" text-anchor="middle" font-family="Roboto Condensed,sans-serif" font-weight="700" font-size="22" fill="#c9a227">START</text></svg>
      <p>Lorem ipsum dolor sit</p>
    </div>
    <div class="abs benefit" style="left:604px;top:2028px">
      <svg viewBox="0 0 80 82" width="80"><g fill="none" stroke="#c9a227" stroke-width="3"><rect x="8" y="2" width="36" height="76" rx="5"/><rect x="22" y="38" width="44" height="28" rx="12"/><path d="M32 52h8M36 48v8"/><circle cx="56" cy="48" r="2"/><circle cx="56" cy="56" r="2"/><circle cx="30" cy="18" r="4"/><rect x="46" y="10" width="7" height="7"/><path d="M62 22l6-4"/></g></svg>
      <p>Lorem ipsum dolor sit</p>
    </div>
    <div class="abs benefit" style="left:814px;top:2028px">
      <svg viewBox="0 0 90 82" width="90"><g fill="none" stroke="#c9a227" stroke-width="3"><rect x="4" y="4" width="82" height="56" rx="3"/><path d="M36 60v12M54 60v12M26 74h38"/><rect x="42" y="18" width="34" height="22" rx="9"/><path d="M50 29h8M54 25v8"/><path d="M14 16l-4 4 4 4M22 16l4 4-4 4M12 32h20M12 40h20M12 48h20"/></g></svg>
      <p>Lorem ipsum dolor sit</p>
    </div>
  </section>

  <section class="cta">
    <div class="abs band"></div>
    <h2 class="abs band-title">Earn power and secure<br>your share today</h2>
    <a class="abs btn band-btn">JOIN NOW</a>
    <div class="abs band-art" role="img" aria-label="Game scene of a forest clearing with a glowing crystal rock"></div>
  </section>

  <section class="partners">
    <div class="abs partner" style="left:122px;top:2798px"><i></i>HEXWARD</div>
    <div class="abs partner" style="left:362px;top:2798px">COINPULSE DAILY</div>
    <div class="abs partner" style="left:600px;top:2798px"><i style="border-radius:50%"></i>TokenLedger</div>
    <div class="abs partner" style="left:906px;top:2798px"><i></i>STRATUM</div>
  </section>

  <footer>
    <div class="abs footer"></div>
    <nav class="abs f-links" style="left:170px;top:3084px;width:100px">Home<br>Wallet<br>Services<br>Game<br>Contact</nav>
    <div class="abs divider" style="left:340px"></div>
    <h3 class="abs center news-title">SIGN UP FOR ALL THE LATEST NEWS AND OFFERS</h3>
    <div class="abs email">Email
      <svg width="18" height="18" viewBox="0 0 18 18"><path d="M1 8L17 1 11 17 8 10z" fill="#7c5cf0"/></svg></div>
    <div class="abs socials" aria-label="Social links"><span></span><span></span><span></span><span></span><span></span></div>
    <p class="abs center copy">©Copyrights 2024&nbsp; Velmora&nbsp;&nbsp; |&nbsp;&nbsp;&nbsp; All Rights Reserved</p>
    <div class="abs divider" style="left:860px"></div>
    <nav class="abs f-links" style="left:892px;top:3084px;width:160px">Terms &amp; Conditions<br>Privacy Policy<br>About Us<br>Support</nav>
  </footer>

</div>
</body>
</html>
```